Business to Business Website Homepage Design

Hi, My Web Developer is giving me designs that aren't quite taking my fancy as far as visual impact. I'd love to see designs come out which are simple, fresh and powerful.
I just want a PDF document that I can give to my web developer to follow, so this project is NOT to make a website, its to design the homepage.
I would like it to scroll down through different areas of my website on the homepage. Our colours are Blood Orange, White, Grey & Black.
I like these websites:
Simplicity
https://www.quenvalo.com/au/webapps/mpp/home
Our Team Section
http://trelmicode.com.au/
We'd like our logo on top left. Nav bar top right. Have an image which we can place a headline subject on + video icon which will pop out with a video and opt in for name and email with a heading so people know what they're opting in for.
The next section should have a lot of white space, this "What we do" which is 1) Grow in size so your business can get bigger 2) increase in value, so you maximise what your business is worth 3) Free up your time, so you can live the lifestyle you've always wanted. Our brief was we want image/text combo with a lot of white space,
Then we have our services
After Services, would like to have a "Why Work With Us" section
Then a testimonials section
Then "Our Team"
Then contact us.
Thats pretty much it, we'd just love some different ideas, these guys are almost there, but just need more impact.
Updates
Target Market(s)
Business Owners between $1m to $3m turnover
Industry/Entity Type
Business
Number of Pages Required
1 page
Look and feel
Each slider illustrates characteristics of the customer's brand and the style your logo design should communicate.

```html
<!DOCTYPE html>
<html lang="en">
<head>
<meta charset="utf-8">
<title>Corvane Partners — Home</title>
<link rel="stylesheet" href="https://fonts.googleapis.com/css2?family=Lato:wght@300;400;700&family=Raleway:wght@400&display=swap">
<style>
  :root {
    --blood-orange: #c42a1f;
    --white: #ffffff;
    --ink: #141414;
    --body-text: #2e2e2e;
    --paper: #f7f5f6;
    --hero-dark: #2c2c2c;
    --hero-mid: #5a5a5a;
    --hero-light: #8a8a8a;
  }
  * { margin: 0; padding: 0; box-sizing: border-box; }
  html, body { width: 1200px; height: 900px; overflow: hidden; }
  body {
    position: relative;
    background: var(--paper);
    font-family: "Lato", sans-serif;
    color: var(--ink);
  }

  /* Hero */
  .hero {
    position: absolute; left: 0; top: 0;
    width: 1200px; height: 515px;
    overflow: hidden;
  }
  .hero-backdrop {
    position: absolute; inset: 0;
    background:
      radial-gradient(ellipse 520px 300px at 600px 230px, rgba(130,130,130,.55), transparent 70%),
      radial-gradient(ellipse 260px 260px at 1080px 380px, rgba(160,150,150,.35), transparent 70%),
      linear-gradient(180deg, var(--hero-mid) 0%, var(--hero-light) 45%, var(--hero-mid) 80%, var(--hero-dark) 100%);
  }
  .hero-backdrop::after {
    content: ""; position: absolute; inset: 0;
    background: linear-gradient(90deg, rgba(20,20,20,.45) 0%, rgba(20,20,20,.1) 40%, rgba(20,20,20,.1) 70%, rgba(20,20,20,.25) 100%);
  }

  .brand {
    position: absolute; left: 135px; top: 14px;
    display: flex; align-items: center; gap: 8px;
  }
  .brand-mark {
    width: 40px; height: 40px; border-radius: 50%;
    background: var(--blood-orange);
  }
  .brand-name {
    font-family: "Lato", sans-serif; font-weight: 700;
    font-size: 17px; letter-spacing: 1.5px;
    color: var(--white); text-transform: uppercase;
    line-height: 1;
  }

  .main-nav {
    position: absolute; right: 148px; top: 33px;
    display: flex; gap: 30px;
  }
  .main-nav a {
    position: relative;
    color: var(--white); text-decoration: none;
    font-weight: 700; font-size: 15px; letter-spacing: .2px;
  }
  .main-nav a.is-active::before {
    content: ""; position: absolute; left: -6px; right: -6px; top: -13px;
    height: 3px; background: var(--blood-orange);
  }
  .main-nav a.is-active::after {
    content: ""; position: absolute; left: 50%; top: -10px;
    margin-left: -4px;
    border-left: 4px solid transparent; border-right: 4px solid transparent;
    border-top: 4px solid var(--blood-orange);
  }

  .hero-headline {
    position: absolute; left: 0; width: 1200px; top: 166px;
    display: flex; justify-content: center; align-items: center;
    font-weight: 400; font-size: 33px; color: var(--white);
    letter-spacing: .3px; line-height: 1;
    padding-left: 0;
  }
  .hero-headline span { display: inline-flex; align-items: center; }
  .hero-headline .marker {
    width: 0; height: 0; margin: 0 10px 0 42px;
    border-left: 8px solid transparent; border-right: 8px solid transparent;
    border-bottom: 10px solid var(--blood-orange);
  }
  .hero-headline .phrase:first-child { margin-left: 17px; }

  .hero-copy {
    position: absolute; left: 245px; width: 710px; top: 251px;
    text-align: center; color: var(--white);
    font-size: 14px; line-height: 23.5px;
  }

  .cta {
    position: absolute; top: 353px;
    width: 178px; height: 49px; border-radius: 25px;
    background: var(--blood-orange); color: var(--white);
    display: flex; align-items: center; justify-content: center;
    font-size: 16px; text-transform: uppercase; text-decoration: none;
  }
  .cta-signup { left: 367px; }
  .cta-subscribe { left: 656px; }

  .video-trigger {
    position: absolute; left: 548px; top: 418px;
    width: 100px; height: 92px;
  }

  /* What we do */
  .what-we-do-title {
    position: absolute; left: 0; width: 1200px; top: 592px;
    text-align: center; font-weight: 400; font-size: 36px;
    color: var(--ink); letter-spacing: -.3px; line-height: 1;
  }
  .feature-media {
    position: absolute; left: 131px; top: 715px;
    width: 433px; height: 200px;
    background: linear-gradient(180deg, #dfe6ec 0%, #c9d3dc 55%, #a9b2bb 100%);
  }
  .feature-title {
    position: absolute; left: 611px; top: 752px; width: 460px;
    font-family: "Raleway", sans-serif; font-weight: 400;
    font-size: 26px; line-height: 45px; color: var(--blood-orange);
    text-transform: uppercase;
  }
  .feature-copy {
    position: absolute; left: 611px; top: 867px; width: 440px;
    font-size: 13px; line-height: 21px; color: var(--body-text);
  }
</style>
</head>
<body>

<header class="hero">
  <div class="hero-backdrop" role="img" aria-label="Photo of a businessman in a suit facing a grey concrete wall sketched with rising arrows, success steps and charts"></div>

  <div class="brand">
    <span class="brand-mark"></span>
    <span class="brand-name">Corvane Partners</span>
  </div>

  <nav class="main-nav">
    <a href="#" class="is-active">HOME</a>
    <a href="#">SERVICES</a>
    <a href="#">EVENTS</a>
    <a href="#">JOBS</a>
    <a href="#">CONTACT</a>
  </nav>

  <h1 class="hero-headline">
    <span class="phrase">YOUR BUSINESS</span>
    <span class="marker"></span>
    <span class="phrase">YOUR SUCCESS</span>
    <span class="marker"></span>
    <span class="phrase">YOUR LIFE</span>
  </h1>

  <p class="hero-copy">Lorem ipsum dolor sit amet, consectetuer adipiscing elit. Aenean commodo ligula eget dolor. Aenean massa. Cum sociis natoque penatibus et magnis dis parturient montes, nascetur ridiculus mus. Donec quam felis, ultricies nec, pellentesque eu, pretium quis, sem.</p>

  <a href="#" class="cta cta-signup">Signup Now</a>
  <a href="#" class="cta cta-subscribe">Subscribe</a>

  <svg class="video-trigger" viewBox="0 0 100 92" aria-label="Play video">
    <g transform="rotate(-35 50 46)">
      <rect x="16" y="24" width="68" height="44" rx="6" fill="#1a1a1a" stroke="#000" stroke-width="2"/>
      <rect x="24" y="29" width="52" height="34" rx="2" fill="#3a3a3a"/>
    </g>
    <circle cx="50" cy="42" r="17" fill="none" stroke="#ffffff" stroke-width="2.5"/>
    <path d="M45 33 L58 42 L45 51 Z" fill="#ffffff"/>
  </svg>
</header>

<main>
  <h2 class="what-we-do-title">WHAT WE DO</h2>

  <div class="feature-media" role="img" aria-label="Photo of business people lifting a rising red growth arrow in front of a city skyline"></div>

  <h3 class="feature-title">Grow in size so your business can get bigger</h3>

  <p class="feature-copy">Lorem ipsum dolor sit amet, consectetuer adipiscing elit. Aenean commodo ligula eget dolor. Aenean massa. Cum sociis natoque penatibus et magnis dis parturient montes.</p>
</main>

</body>
</html>
```